Accounting business needs business card

I have a business card but need something better. I want the colour changed and the design to be better. I have uploaded a picture of my new sign that is grey in colour, i would like to incorporate these colours.

```html
<!DOCTYPE html>
<html lang="en">
<head>
<meta charset="utf-8">
<title>Ledge Tax — Business Card</title>
<link href="https://fonts.googleapis.com/css2?family=Montserrat:wght@400;500;700;800&display=swap" rel="stylesheet">
<style>
  :root {
    --backdrop: #d6d6d6;
    --card-light: #f3f3f3;
    --card-dark-top: #4b4b4d;
    --card-dark-bottom: #343436;
    --ink: #141414;
    --ink-soft: #2a2a2a;
    --silver: #d9d9d9;
    --silver-dim: #a9a9ab;
    --badge-blue: #1c4d9c;
    --badge-cyan: #1aa3e0;
  }
  * { box-sizing: border-box; margin: 0; padding: 0; }
  html, body {
    width: 1200px; height: 800px; overflow: hidden;
    background: var(--backdrop);
    font-family: "Montserrat", sans-serif;
  }
  .canvas {
    width: 1200px; height: 800px;
    display: flex; align-items: center; justify-content: center; gap: 40px;
  }
  .card {
    width: 540px; height: 310px;
    border-radius: 4px;
    position: relative;
    box-shadow: 0 10px 24px rgba(0,0,0,0.18);
  }
  /* Front */
  .card--front {
    background: var(--card-light);
    display: flex; align-items: center;
    padding: 0 34px 0 40px;
  }
  .brand {
    width: 200px;
    display: flex; flex-direction: column; align-items: center;
    color: var(--ink);
  }
  .brand__mark {
    width: 86px; height: 86px;
    border: 3px solid currentColor; border-radius: 50%;
    margin-bottom: 22px;
  }
  .brand__name {
    font-weight: 500; font-size: 26px; letter-spacing: 10px;
    margin-right: -10px; white-space: nowrap;
  }
  .divider {
    width: 1.5px; height: 150px; background: var(--ink);
    margin: 0 26px 0 22px; flex-shrink: 0;
  }
  .contact { color: var(--ink); }
  .contact__name {
    font-weight: 800; font-size: 19px; letter-spacing: 0.5px;
    text-transform: uppercase;
  }
  .contact__creds { font-size: 11.5px; font-weight: 500; margin-top: 4px; }
  .contact__role { font-size: 11.5px; font-weight: 500; margin-top: 2px; }
  .contact__list { list-style: none; margin-top: 22px; }
  .contact__item {
    display: flex; align-items: center; gap: 9px;
    font-size: 11.5px; font-weight: 500; color: var(--ink-soft);
    margin-bottom: 5px;
  }
  .contact__icon { width: 12px; height: 12px; flex-shrink: 0; }
  /* Back */
  .card--back {
    background: linear-gradient(160deg, var(--card-dark-top), var(--card-dark-bottom));
    display: flex; flex-direction: column; align-items: center; justify-content: center;
  }
  .card--back .brand { width: auto; color: var(--silver); }
  .card--back .brand__mark { width: 96px; height: 96px; border-color: var(--silver-dim); margin-bottom: 20px; }
  .card--back .brand__name { font-size: 30px; letter-spacing: 13px; margin-right: -13px; }
  .badges { display: flex; align-items: center; gap: 8px; margin-top: 22px; }
  .badge--listing { width: 92px; height: 36px; background: var(--badge-blue); }
  .badge--partner { width: 40px; height: 40px; border-radius: 50%; background: var(--badge-cyan); }
</style>
</head>
<body>
<main class="canvas">
  <section class="card card--front" aria-label="Business card front">
    <div class="brand">
      <div class="brand__mark"></div>
      <div class="brand__name">LEDGE TAX</div>
    </div>
    <div class="divider"></div>
    <div class="contact">
      <h1 class="contact__name">Owen Halloway</h1>
      <p class="contact__creds">CPA, MTAX, BCOM (Acc &amp; Fin)</p>
      <p class="contact__role">Taxation &amp; Business Accountant</p>
      <ul class="contact__list">
        <li class="contact__item">
          <svg class="contact__icon" viewBox="0 0 24 24" aria-hidden="true"><path fill="currentColor" d="M6.6 10.8a15.1 15.1 0 0 0 6.6 6.6l2.2-2.2c.3-.3.7-.4 1-.2 1.1.4 2.3.6 3.6.6.6 0 1 .4 1 1V20c0 .6-.4 1-1 1A17 17 0 0 1 3 4c0-.6.4-1 1-1h3.5c.6 0 1 .4 1 1 0 1.3.2 2.5.6 3.6.1.3 0 .7-.2 1z"/></svg>
          0412 555 019
        </li>
        <li class="contact__item">
          <svg class="contact__icon" viewBox="0 0 24 24" aria-hidden="true"><path fill="currentColor" d="M2 5h20v14H2z"/><path d="M2 5l10 8 10-8" fill="none" stroke="#f3f3f3" stroke-width="2"/></svg>
          owen@ledgetax.com.au
        </li>
        <li class="contact__item">
          <svg class="contact__icon" viewBox="0 0 24 24" aria-hidden="true"><circle cx="12" cy="12" r="10" fill="currentColor"/><path d="M2 12h20M12 2c3 3 3 17 0 20M12 2c-3 3-3 17 0 20" fill="none" stroke="#f3f3f3" stroke-width="1.5"/></svg>
          www.ledgetax.com.au
        </li>
      </ul>
    </div>
  </section>

  <section class="card card--back" aria-label="Business card back">
    <div class="brand">
      <div class="brand__mark"></div>
      <div class="brand__name">LEDGE TAX</div>
    </div>
    <div class="badges">
      <div class="badge badge--listing" role="img" aria-label="Professional membership badge"></div>
      <div class="badge badge--partner" role="img" aria-label="Software partner badge"></div>
    </div>
  </section>
</main>
</body>
</html>
```